Volren Goods Ltd Stationery Design Project

hi we need to design business cards, letter head, complimentary slips, scribble pads, note pads, envelopes for volren goods ltd.

please see business cards details

Kelvin Obutu

P.O Box 41873 -00312 Nairobi - Kenya
Tel: +254-733-218-904
Email: volrengoods@mailvexo.com

company name should appear on all stationery : Volren Goods Ltd

Industry/Entity Type

Business

Requirements
Must have
• kindly stick to colours in the logo

```html
<!DOCTYPE html>
<html lang="en">
<head>
<meta charset="utf-8">
<title>Volren Goods Ltd — Presentation Folder</title>
<link rel="stylesheet" href="https://fonts.googleapis.com/css2?family=Montserrat:wght@500;700;800&display=swap">
<style>
  :root {
    --brand-blue: #2e3192;
    --brand-blue-light: #4a4fb0;
    --brand-orange: #f7941d;
    --brand-orange-light: #fbb040;
    --paper-white: #ffffff;
    --stage-top: #d9dadc;
    --stage-bottom: #ffffff;
    --label-ink: #2e3192;
    --font-main: "Montserrat", Arial, sans-serif;
  }
  * { box-sizing: border-box; margin: 0; padding: 0; }
  html, body { width: 1200px; height: 1000px; overflow: hidden; }
  body {
    position: relative;
    font-family: var(--font-main);
    background: linear-gradient(to bottom, var(--stage-top) 0%, var(--stage-bottom) 45%);
  }

  .spread { position: absolute; display: flex; box-shadow: 0 18px 24px rgba(0,0,0,.18); }
  .spread--outside { left: 480px; top: 78px; width: 670px; height: 512px; }
  .spread--inside  { left: 50px;  top: 430px; width: 670px; height: 500px; }

  .panel { position: relative; width: 50%; height: 100%; overflow: hidden; }
  .panel--blue   { background: var(--brand-blue); }
  .panel--orange { background: var(--brand-orange); }

  .piece-label {
    position: absolute; font-size: 9px; font-weight: 700; color: var(--label-ink); white-space: nowrap;
  }
  .piece-label--back   { left: 480px; top: 62px; }
  .piece-label--front  { left: 1081px; top: 62px; }
  .piece-label--inside { left: 350px; top: 434px; }

  .wordmark {
    position: absolute; left: 0; right: 0; top: 32px; text-align: center;
    font-weight: 800; font-size: 20px; line-height: 1.05; letter-spacing: 1px;
    color: var(--paper-white); text-transform: uppercase;
  }

  .sun-ornament {
    position: absolute; left: 50%; bottom: 0; width: 270px; height: 160px; transform: translateX(-50%);
    border-radius: 135px 135px 0 0;
  }
  .sun-ornament--on-blue   { background: radial-gradient(ellipse at 50% 100%, var(--brand-blue-light) 0%, rgba(74,79,176,.5) 45%, rgba(46,49,146,0) 75%); }
  .sun-ornament--on-orange { background: radial-gradient(ellipse at 50% 100%, var(--brand-orange-light) 0%, rgba(251,176,64,.55) 45%, rgba(247,148,29,0) 75%); }

  .contact-line {
    position: absolute; left: 14px; bottom: 10px; font-size: 6px; font-weight: 500;
    color: var(--brand-orange); white-space: nowrap;
  }

  .pocket {
    position: absolute; left: 0; bottom: 0; width: 100%; height: 195px;
    background: var(--brand-blue);
    clip-path: polygon(0 0, 74% 0, 88% 22%, 88% 40%, 100% 58%, 100% 100%, 0 100%);
    box-shadow: 0 -6px 10px rgba(0,0,0,.2);
  }
  .card-label { position: absolute; left: 122px; top: 40px; font-size: 7px; font-weight: 700; color: var(--paper-white); }

  .business-card {
    position: absolute; left: 92px; top: 50px; width: 172px; height: 100px; display: flex;
    box-shadow: 0 3px 6px rgba(0,0,0,.3);
  }
  .business-card__brand {
    width: 50%; background: var(--paper-white); display: flex; align-items: center; justify-content: center;
    font-weight: 800; font-size: 11px; line-height: 1.05; color: var(--brand-orange); text-align: center; text-transform: uppercase;
  }
  .business-card__details { width: 50%; background: var(--brand-orange); position: relative; }
  .business-card__name {
    position: absolute; top: 14px; left: 8px; right: 0; background: var(--brand-blue); color: var(--brand-orange);
    padding: 3px 4px; font-size: 5px; font-weight: 700; line-height: 1.3;
  }
  .business-card__contacts {
    position: absolute; left: 8px; top: 54px; list-style: none; font-size: 4px; line-height: 1.6; color: var(--brand-blue); font-weight: 500;
  }
</style>
</head>
<body>

  <span class="piece-label piece-label--back">Folder (Back)</span>
  <span class="piece-label piece-label--front">Folder (Front)</span>

  <section class="spread spread--outside" aria-label="Folder outside">
    <div class="panel panel--blue">
      <div class="sun-ornament sun-ornament--on-blue" role="img" aria-label="Faint swirling sun ornament"></div>
      <p class="contact-line">P.O Box 41873 -00312 Nairobi - Kenya &nbsp;· Tel: +254-733-218-904 &nbsp;· Email: volrengoods@mailvexo.com</p>
    </div>
    <div class="panel panel--orange">
      <h1 class="wordmark">Volren<br>Goods</h1>
      <div class="sun-ornament sun-ornament--on-orange" role="img" aria-label="Faint swirling sun ornament"></div>
    </div>
  </section>

  <section class="spread spread--inside" aria-label="Folder inside">
    <div class="panel panel--orange">
      <div class="pocket">
        <span class="card-label">Business Card #2</span>
        <div class="business-card">
          <div class="business-card__brand">Volren<br>Goods</div>
          <div class="business-card__details">
            <p class="business-card__name">Kelvin Obutu<br>CEO / Founder</p>
            <ul class="business-card__contacts">
              <li>P.O Box 41873 -00312</li>
              <li>Nairobi - Kenya</li>
              <li>+254-733-218-904</li>
              <li>volrengoods@mailvexo.com</li>
            </ul>
          </div>
        </div>
        <p class="contact-line">P.O Box 41873 -00312 Nairobi - Kenya &nbsp;· Tel: +254-733-218-904 &nbsp;· Email: volrengoods@mailvexo.com</p>
      </div>
    </div>
    <div class="panel panel--orange">
      <div class="sun-ornament sun-ornament--on-orange" role="img" aria-label="Faint swirling sun ornament"></div>
    </div>
  </section>

  <span class="piece-label piece-label--inside">Folder (Inside)</span>

</body>
</html>
```